Safety Starts at The Top

Want to make a poster showing our company president in full safety gear (see attached photo) encouraging how "Safety Starts at the Top" We encourage creativity. Visit our website for ideas about our company. www.halvorbuilders.com Our main colors are blue and black, but we will allow other colors to make the poster pop and stand out.

Industry/Entity Type

It Company

Colors
0255a3

Requirements
Must have
• -Must have the photo attached somewhere on the poster. Must have a PPE List which can be creative or bullet points 1. Hard Hat 2. Safety Glasses 3. Shirt with Sleeves, 4. Reflective Vest 5. Gloves 6. Long Pants 7. Safety Boots
• -Must have title "Safety Starts at the Top"
• -Must have a box or section that says the following"Because of our company's core value of RESPECT FOR ALL PEOPLE the commitment to Safety Starts at the Top. Halvor Builders’s most valuable asset is our team members, which is why I take personal responsibility for our safety culture. It is our daily mission for every team member to return home to their families without injuries, giving them a life away from work that can be enjoyed."

```html
<!DOCTYPE html>
<html lang="en">
<head>
<meta charset="utf-8">
<title>Safety Starts at the Top — Halvor Builders</title>
<link href="https://fonts.googleapis.com/css2?family=Oswald:wght@600;700&family=Titan+One&display=swap" rel="stylesheet">
<style>
  :root {
    --paper: #ffffff;
    --ink: #000000;
    --brand-blue: #0255a3;
    --glow-blue: #1a6fd0;
    --safety-yellow: #fff200;
    --quote-text: #ffffff;
  }
  * { margin: 0; padding: 0; box-sizing: border-box; }
  html, body { width: 821px; height: 1200px; overflow: hidden; background: var(--paper); }
  .poster {
    position: absolute; left: 32px; top: 32px; width: 757px; height: 1136px;
    background: linear-gradient(180deg,
      var(--ink) 0%, #02152c 12%, #04316a 30%, var(--brand-blue) 46%,
      var(--glow-blue) 53%, var(--brand-blue) 62%, #033a78 74%, #011022 88%, var(--ink) 100%);
    overflow: hidden;
  }
  .poster-title {
    position: absolute; left: -100px; right: -100px; top: 22px; text-align: center;
    white-space: nowrap;
    font-family: "Oswald", sans-serif; font-weight: 700; font-size: 88px;
    line-height: 1; letter-spacing: -1px; color: var(--safety-yellow);
    transform: scaleX(0.75);
    transform-origin: center top;
  }
  .quote-panel {
    position: absolute; left: 54px; top: 151px; width: 662px; height: 392px;
    background: var(--ink); border: 5px solid var(--paper); border-radius: 40px;
  }
  .quote-text {
    position: absolute; left: 25px; top: 38px; width: 345px;
    font-family: "Oswald", sans-serif; font-weight: 600; font-size: 18px;
    line-height: 24.6px; color: var(--quote-text);
  }
  .president-photo {
    position: absolute; left: 410px; top: 26px; width: 222px; height: 332px;
    border: 2px solid var(--paper);
    background: linear-gradient(180deg, #4a4a4c 0%, #6b6a66 45%, #3a3a3a 100%);
  }
  .ppe-list { position: absolute; left: 130px; top: 560px; list-style: none; }
  .ppe-item {
    display: flex; align-items: center; height: 76.4px; white-space: nowrap;
    font-family: "Titan One", sans-serif; font-size: 47px; color: var(--safety-yellow);
    -webkit-text-stroke: 2px var(--ink); paint-order: stroke fill;
    text-shadow: 3px 3px 0 var(--ink), -2px -2px 0 var(--ink), 2px -2px 0 var(--ink), -2px 2px 0 var(--ink);
  }
  .ppe-check { width: 66px; height: 66px; margin-right: 18px; flex: none; }
</style>
</head>
<body>
<main class="poster">
  <h1 class="poster-title">SAFETY STARTS AT THE TOP</h1>

  <section class="quote-panel">
    <p class="quote-text">"Because of our company's core value of RESPECT FOR ALL PEOPLE the commitment to Safety Starts at the Top. Halvor Builders’s most valuable asset is our team members, which is why I take personal responsibility for our safety culture. It is our daily mission for every team member to return home to their families without injuries, giving them a life away from work that can be enjoyed."</p>
    <div class="president-photo" role="img" aria-label="Photo of the company president standing in a warehouse wearing a hard hat, safety glasses, reflective vest, gloves, long pants and safety boots"></div>
  </section>

  <svg width="0" height="0" style="position:absolute">
    <defs>
      <symbol id="check-box" viewBox="0 0 68 68">
        <rect x="6" y="10" width="50" height="50" rx="12" fill="none" stroke="#000" stroke-width="12"/>
        <rect x="6" y="10" width="50" height="50" rx="12" fill="none" stroke="#fff" stroke-width="6"/>
        <path d="M18 34 L30 47 L60 6" fill="none" stroke="#000" stroke-width="14" stroke-linecap="round" stroke-linejoin="round"/>
        <path d="M18 34 L30 47 L60 6" fill="none" stroke="#fff" stroke-width="7" stroke-linecap="round" stroke-linejoin="round"/>
      </symbol>
    </defs>
  </svg>

  <ul class="ppe-list">
    <li class="ppe-item"><svg class="ppe-check"><use href="#check-box"/></svg>Hard Hat</li>
    <li class="ppe-item"><svg class="ppe-check"><use href="#check-box"/></svg>Safety Glasses</li>
    <li class="ppe-item"><svg class="ppe-check"><use href="#check-box"/></svg>Shirt with Sleeves</li>
    <li class="ppe-item"><svg class="ppe-check"><use href="#check-box"/></svg>Reflective Vest</li>
    <li class="ppe-item"><svg class="ppe-check"><use href="#check-box"/></svg>Gloves</li>
    <li class="ppe-item"><svg class="ppe-check"><use href="#check-box"/></svg>Long Pants</li>
    <li class="ppe-item"><svg class="ppe-check"><use href="#check-box"/></svg>Safety Boots</li>
  </ul>
</main>
</body>
</html>
```